Need wine label for brand that is named: Casmerel Vineyards & Winery

Casmerel is a yoga way of breathing. In Sanskrit Casmerel means "flying up." I would like a creative wine label that articulates Casmerel. The label should include a graphic and the name Casmerel on one line and Vineyards & Winery in smaller print underneath Casmerel.

```html
<!DOCTYPE html>
<html lang="en">
<head>
<meta charset="utf-8">
<title>Casmerel Vineyards &amp; Winery – Wine Label</title>
<link href="https://fonts.googleapis.com/css2?family=Josefin+Sans:wght@300;400&display=swap" rel="stylesheet">
<style>
  :root {
    --page: #f4f2f3;
    --magenta: #ff14b0;
    --magenta-deep: #c42a8e;
    --cloud-light: #f6c2e4;
    --cloud-mid: #df63b6;
    --band: #d94ba8;
    --band-light: #e981c6;
    --white: #ffffff;
    --subtitle: #f07ccb;
  }
  html, body {
    margin: 0;
    padding: 0;
    width: 1200px;
    height: 2243px;
    overflow: hidden;
    background: var(--page);
  }
  .label {
    position: relative;
    width: 1200px;
    height: 2243px;
  }
  .label-art {
    position: absolute;
    inset: 0;
    width: 1200px;
    height: 2243px;
  }
  .brand-name {
    position: absolute;
    left: 0;
    width: 1200px;
    top: 1128px;
    margin: 0;
    text-align: center;
    font-family: "Josefin Sans", sans-serif;
    font-weight: 300;
    font-size: 104px;
    letter-spacing: 10px;
    line-height: 1;
    color: var(--white);
  }
  .brand-sub {
    position: absolute;
    left: 0;
    width: 1200px;
    top: 1318px;
    margin: 0;
    text-align: center;
    font-family: "Josefin Sans", sans-serif;
    font-weight: 300;
    font-size: 50px;
    letter-spacing: 5px;
    line-height: 1;
    color: var(--subtitle);
  }
</style>
</head>
<body>
<main class="label">
  <svg class="label-art" viewBox="0 0 1200 2243" xmlns="http://www.w3.org/2000/svg">
    <defs>
      <radialGradient id="sky-upper" cx="0.5" cy="0.55" r="0.65">
        <stop offset="0" stop-color="var(--cloud-light)"/>
        <stop offset="0.55" stop-color="var(--cloud-mid)"/>
        <stop offset="1" stop-color="var(--magenta-deep)"/>
      </radialGradient>
      <radialGradient id="sky-lower" cx="0.5" cy="0.5" r="0.7">
        <stop offset="0" stop-color="var(--cloud-light)"/>
        <stop offset="0.5" stop-color="var(--cloud-mid)"/>
        <stop offset="1" stop-color="var(--magenta-deep)"/>
      </radialGradient>
      <linearGradient id="title-band" x1="0" y1="0" x2="0" y2="1">
        <stop offset="0" stop-color="var(--band-light)"/>
        <stop offset="1" stop-color="var(--band)"/>
      </linearGradient>
    </defs>

    <!-- arched label frame -->
    <path class="label-frame" fill="var(--magenta)"
      d="M600,130 C620,210 700,290 808,330 L808,440 L892,440 C900,520 1000,600 1100,651 L1100,2110 L100,2110 L100,651 C200,600 300,520 308,440 L392,440 L392,330 C500,290 580,210 600,130 Z"/>

    <!-- crown diamond -->
    <path class="crown-diamond" fill="var(--white)" d="M600,218 L622,240 L600,262 L578,240 Z"/>

    <!-- upper sky window -->
    <path class="sky-window-upper" role="img" aria-label="Mirrored pink clouds rising into the sky"
      fill="url(#sky-upper)"
      d="M600,300 C618,360 690,420 770,450 L770,520 L850,520 C860,590 960,660 1042,700 L1042,1061 L158,1061 L158,700 C240,660 340,590 350,520 L430,520 L430,450 C510,420 582,360 600,300 Z"/>

    <!-- title band -->
    <rect class="title-band" x="158" y="1061" width="884" height="341" fill="url(#title-band)"/>
    <line class="title-rule" x1="330" y1="1108" x2="870" y2="1108" stroke="var(--white)" stroke-width="3"/>

    <!-- lower sky window -->
    <rect class="sky-window-lower" role="img" aria-label="Mirrored pink clouds drifting upward"
      x="158" y="1402" width="884" height="563" fill="url(#sky-lower)"/>

    <!-- footer diamonds -->
    <g class="footer-diamonds" fill="var(--white)">
      <path d="M416,2022 L436,2042 L416,2062 L396,2042 Z"/>
      <path d="M508,2022 L528,2042 L508,2062 L488,2042 Z"/>
      <path d="M600,2022 L620,2042 L600,2062 L580,2042 Z"/>
      <path d="M692,2022 L712,2042 L692,2062 L672,2042 Z"/>
      <path d="M784,2022 L804,2042 L784,2062 L764,2042 Z"/>
    </g>
  </svg>

  <h1 class="brand-name">CASMEREL</h1>
  <p class="brand-sub">VINEYARDS &amp; WINERY</p>
</main>
</body>
</html>
```